【依頼の目的/概要】
電子書籍(bookrie)の表紙デザインをお願いします。

【画像サイズ】※BRPより抜粋
表紙ファイルの理想的な寸法は2,560×1,600ピクセルです。
注:画像の寸法は10,000×10,000ピクセルです。

【タイトル】
資格試験 ゴールダッシュ・速習・楽々学習術

サブタイトル
通れる学び方

【著者】
行政書士 社会保険労務士
森川澄江

【本の内容】
行政書士試験の勉強を短期間で仕上げて、合格する勉強法を
書いた本です。

【デザイン要望】
特にこだわりません。
素敵なデザインの応募を楽しみにしています。
※次点、次々点の方への参加報酬を設定しました。

その他
必要な情報がありましたらお問い合わせください。

本を以下に添付します。
本文中にエクセルで作成した表を挿入します。

明るく見やすく、わかり易い表現が良かったです。

皆様お疲れ様でした。
T_okabe様には訂正を速攻して頂きありがとうございました。
最後まで迷いました。
皆様のご依頼が増えますことをご祈念申し上げます。

```html
<!DOCTYPE html>
<html lang="ja">
<head>
<meta charset="UTF-8">
<title>資格試験 ゴールダッシュ・速習・楽々学習術</title>
<link href="https://fonts.googleapis.com/css2?family=Noto+Sans+JP:wght@500;700;900&display=swap" rel="stylesheet">
<style>
  :root{
    --cream:#fbf5e4;
    --white:#ffffff;
    --orange:#e8572a;
    --brown:#4a3326;
    --yellow:#fde84a;
    --peach:#f6c9b4;
    --pink:#ee9a93;
  }
  *{margin:0;padding:0;box-sizing:border-box}
  html,body{width:749px;height:1200px;overflow:hidden}
  body{background:var(--cream);font-family:"Noto Sans JP",sans-serif;color:var(--brown)}
  .cover{position:relative;width:749px;height:1200px;overflow:hidden;background:var(--cream)}
  .frame{position:absolute;left:50px;top:120px;width:650px;height:880px;background:var(--white);border:3px solid var(--orange);border-radius:22px 22px 0 0;border-bottom:none}
  .series{position:absolute;left:88px;top:12px;width:574px;height:118px;background:var(--orange);color:var(--white);font-weight:900;font-size:98px;line-height:118px;text-align:center;letter-spacing:8px}
  .lead{position:absolute;left:0;top:160px;width:749px;text-align:center;font-weight:700;font-size:60px;letter-spacing:2px}
  .lead-arc{position:absolute;left:150px;top:150px;width:450px;height:110px}
  .quick{position:absolute;left:180px;top:275px;width:96px;height:168px;background:var(--orange);color:var(--white);font-weight:900;font-size:70px;line-height:80px;text-align:center;padding-top:4px}
  .easy-mark{position:absolute;left:290px;top:385px;width:370px;height:38px;background:var(--yellow)}
  .easy{position:absolute;left:285px;top:240px;font-weight:900;font-size:185px;line-height:200px;letter-spacing:-4px}
  .method{position:absolute;left:0;top:455px;width:749px;text-align:center;font-weight:900;font-size:200px;line-height:215px;letter-spacing:-6px}
  .figure{position:absolute;left:365px;top:670px;width:250px;height:330px;border-radius:120px 120px 0 0;background:linear-gradient(180deg,var(--peach),var(--pink))}
  .badge{position:absolute;left:560px;top:620px;width:186px;height:186px;border-radius:50%;background:var(--white);border:4px solid var(--orange);text-align:center;padding-top:30px;font-weight:700;font-size:22px;line-height:30px}
  .badge .accent{color:var(--orange);font-size:26px;font-weight:900}
  .author{position:absolute;left:25px;top:860px;font-weight:500;font-size:25px;line-height:32px}
  .author .name{font-weight:700;font-size:46px;line-height:62px}
  .author .name small{font-size:24px;font-weight:500;margin-left:6px}
  .band{position:absolute;left:0;top:1000px;width:749px;height:200px;background:var(--yellow);text-align:center}
  .band .subtitle{font-weight:900;font-size:88px;line-height:110px;padding-top:8px;letter-spacing:6px}
  .band .note{font-weight:700;font-size:33px;line-height:40px}
</style>
</head>
<body>
<main class="cover">
  <div class="frame"></div>
  <div class="series">資格試験</div>
  <svg class="lead-arc" viewBox="0 0 450 110" aria-hidden="true">
    <path d="M10 95 Q60 20 120 15" fill="none" stroke="var(--orange)" stroke-width="3"/>
    <path d="M440 95 Q390 20 330 15" fill="none" stroke="var(--orange)" stroke-width="3"/>
  </svg>
  <div class="lead">ゴールダッシュ</div>
  <div class="quick">速<br>習</div>
  <div class="easy-mark"></div>
  <div class="easy">楽々</div>
  <div class="method">学習術</div>
  <div class="figure" role="img" aria-label="ペンを持って勉強する女性のイラスト"></div>
  <div class="badge">合格出来る!<br>受かる!<br><span class="accent">勉強方法と<br>テクニック</span></div>
  <div class="author">行政書士<br>社会保険労務士<div class="name">森川澄江<small>著</small></div></div>
  <div class="band">
    <div class="subtitle">通れる学び方</div>
    <div class="note">受験ではテクニックを<br>知っているのと知らないのは雲泥の差!</div>
  </div>
</main>
</body>
</html>
```